Bref créative
Brightfield Signal STATIONARY
business cards and letterhead
Professional
Alan Vortmeyer
President
4172 Tamsin Street
Harlow Bay, Northmere
L3P 7R2
alan@brightfieldsignal.ca
brightfieldsignal.ca

```html
<!DOCTYPE html>
<html lang="en">
<head>
<meta charset="utf-8">
<title>Brightfield Signal Stationery</title>
<link href="https://fonts.googleapis.com/css2?family=Titillium+Web:wght@400;700&family=Open+Sans:wght@400;600&display=swap" rel="stylesheet">
<style>
  :root {
    --bg: #eceef1;
    --paper: #ffffff;
    --blue: #1d95e6;
    --blue-light: #5cc3f7;
    --blue-deep: #137fd0;
    --ink: #3a4a5c;
    --grey: #8a96a3;
    --band-rule: #8e98a2;
    --shadow: 0 6px 18px rgba(40, 60, 80, 0.18);
  }
  * { margin: 0; padding: 0; box-sizing: border-box; }
  html, body { width: 1200px; height: 936px; overflow: hidden; background: var(--bg); }
  body { position: relative; font-family: "Open Sans", Arial, sans-serif; color: var(--ink); }

  .piece { position: absolute; background: var(--paper); box-shadow: var(--shadow); overflow: hidden; }

  .brand { display: flex; align-items: center; gap: 8px; white-space: nowrap; }
  .brand-dot { border-radius: 50%; background: var(--blue); flex: none; }
  .brand-name { font-family: "Titillium Web", Arial, sans-serif; font-weight: 700; color: var(--blue-deep); text-transform: uppercase; letter-spacing: 0.02em; line-height: 1; white-space: nowrap; }

  .contact-list { list-style: none; font-size: 7px; line-height: 12px; color: var(--grey); white-space: nowrap; }
  .contact-list li { display: flex; align-items: flex-start; gap: 5px; }
  .contact-list li::before { content: ""; width: 6px; height: 6px; margin-top: 3px; border-radius: 50%; background: var(--blue); flex: none; }

  /* Letterhead */
  .letterhead { left: 182px; top: 71px; width: 418px; height: 544px; }
  .letterhead .brand { position: absolute; left: 24px; top: 26px; }
  .letterhead .brand-dot { width: 30px; height: 30px; }
  .letterhead .brand-name { font-size: 15px; }
  .letterhead .contact-list { position: absolute; left: 262px; top: 22px; }
  .letterhead-mark { position: absolute; left: 162px; top: 222px; width: 96px; height: 96px; border-radius: 50%; background: radial-gradient(circle at 40% 35%, #f6f8fa, #e1e6ea); }

  /* Folder */
  .folder { left: 634px; top: 38px; width: 461px; height: 578px; background: linear-gradient(180deg, var(--blue-light) 0%, var(--blue) 55%, var(--blue-deep) 100%); }
  .folder-band { position: absolute; left: 0; right: 0; top: 233px; height: 122px; background: var(--paper); border-bottom: 8px solid var(--band-rule); display: flex; align-items: center; padding-left: 56px; }
  .folder-band .brand { gap: 12px; }
  .folder-band .brand-dot { width: 80px; height: 80px; }
  .folder-band .brand-name { font-size: 27px; }

  /* Business cards */
  .card { left: 46px; width: 190px; height: 83px; }
  .card-front { top: 654px; }
  .card-back { top: 779px; }
  .card-top { position: absolute; left: 0; right: 0; top: 0; height: 40px; padding: 9px 0 0 10px; }
  .card .brand { gap: 5px; }
  .card .brand-dot { width: 18px; height: 18px; }
  .card .brand-name { font-size: 9px; }
  .card-strip { position: absolute; left: 0; right: 0; bottom: 0; height: 43px; background: linear-gradient(180deg, var(--blue-light), var(--blue)); }
  .card-person { position: absolute; left: 10px; top: 8px; color: var(--paper); white-space: nowrap; }
  .card-person .name { font-size: 7px; font-weight: 600; }
  .card-person .title { font-size: 5.5px; }
  .card-front .contact-list { position: absolute; left: 98px; top: 5px; font-size: 5px; line-height: 8px; color: var(--paper); }
  .card-front .contact-list li::before { background: var(--paper); width: 4px; height: 4px; margin-top: 2px; }
  .card-back .brand { position: absolute; left: 10px; top: 12px; }
  .card-back .card-strip { height: 26px; display: flex; align-items: center; justify-content: center; }
  .card-url { font-size: 6px; letter-spacing: 0.25em; color: var(--paper); white-space: nowrap; }

  /* Envelope front */
  .envelope-front { left: 261px; top: 667px; width: 348px; height: 195px; }
  .envelope-front .brand { position: absolute; left: 18px; top: 18px; }
  .envelope-front .brand-dot { width: 26px; height: 26px; }
  .envelope-front .brand-name { font-size: 12px; }
  .envelope-front .address { position: absolute; left: 18px; top: 52px; font-size: 6.5px; color: var(--grey); white-space: nowrap; }

  /* Envelope back */
  .envelope-back { left: 631px; top: 667px; width: 523px; height: 195px; }
  .envelope-back svg { position: absolute; inset: 0; }
  .envelope-url { position: absolute; left: 0; right: 0; top: 20px; text-align: center; font-size: 10px; letter-spacing: 0.3em; color: var(--paper); white-space: nowrap; }
</style>
</head>
<body>

  <section class="piece letterhead">
    <div class="brand">
      <span class="brand-dot"></span>
      <span class="brand-name">Brightfield Signal</span>
    </div>
    <ul class="contact-list">
      <li>4172 Tamsin Street Harlow Bay,<br>Northmere L3P 7R2</li>
      <li>(905) 555-0148</li>
      <li>alan@brightfieldsignal.ca</li>
      <li>www.brightfieldsignal.ca</li>
    </ul>
    <div class="letterhead-mark"></div>
  </section>

  <section class="piece folder">
    <div class="folder-band">
      <div class="brand">
        <span class="brand-dot"></span>
        <span class="brand-name">Brightfield Signal</span>
      </div>
    </div>
  </section>

  <section class="piece card card-front">
    <div class="card-top">
      <div class="brand">
        <span class="brand-dot"></span>
        <span class="brand-name">Brightfield Signal</span>
      </div>
    </div>
    <div class="card-strip">
      <div class="card-person">
        <div class="name">Alan Vortmeyer</div>
        <div class="title">President</div>
      </div>
      <ul class="contact-list">
        <li>4172 Tamsin Street, Harlow Bay</li>
        <li>(905) 555-0148</li>
        <li>alan@brightfieldsignal.ca</li>
        <li>brightfieldsignal.ca</li>
      </ul>
    </div>
  </section>

  <section class="piece card card-back">
    <div class="brand">
      <span class="brand-dot"></span>
      <span class="brand-name">Brightfield Signal</span>
    </div>
    <div class="card-strip">
      <span class="card-url">www.brightfieldsignal.ca</span>
    </div>
  </section>

  <section class="piece envelope-front">
    <div class="brand">
      <span class="brand-dot"></span>
      <span class="brand-name">Brightfield Signal</span>
    </div>
    <p class="address">4172 Tamsin Street Harlow Bay, Northmere L3P 7R2</p>
  </section>

  <section class="piece envelope-back">
    <svg width="523" height="195" viewBox="0 0 523 195">
      <defs>
        <linearGradient id="flapBlue" x1="0" y1="0" x2="0" y2="1">
          <stop offset="0" stop-color="#5cc3f7"/>
          <stop offset="1" stop-color="#1d95e6"/>
        </linearGradient>
      </defs>
      <path d="M0 195 L230 95 Q261 82 292 95 L523 195" fill="none" stroke="#dfe4e8" stroke-width="1.5"/>
      <path d="M0 0 L523 0 L290 108 Q261 120 232 108 Z" fill="url(#flapBlue)"/>
    </svg>
    <div class="envelope-url">www.brightfieldsignal.ca</div>
  </section>

</body>
</html>
```